KELBROOK PAINTING

We are a painting company. We paint residential, commercial and strata jobs. I need the website to be very sharp, neat and elegant. I've attached our logo. the Logo needs to be embossed as a gold color and the background like a Matt black. I need these tabs:

• HOME • ABOUT US • SERVICES • TESTIMONIALS • SHOWCASE • CONTACT US

Be creative and innovative in your style.
take this as an example to just get the gist of what I'm expecting. If you can better it then the job is yours!

http://gilmarchcoatings.com.au/contact.html

I look forward to seeing your artwork :)

#These are the links to my logo in PSD format.

https://www.filevaultzy.com/s/qrtxwpl3k8hvb2z/Kelbrook%20Painting%20Luxury%20Gold.rar

https://www.filevaultzy.com/sh/hvbdkwpa2m7ycq5/XuoP7-bqLk

Painting

• Making the Logo embossed like the artworks i have attached is definitely a necessity.

Can you let me know if this is possible to apply to the website.

thank you

```html
<!DOCTYPE html>
<html lang="en">
<head>
<meta charset="utf-8">
<title>Kelbrook Painting</title>
<link href="https://fonts.googleapis.com/css2?family=Questrial&family=Arimo:ital@0;1&display=swap" rel="stylesheet">
<style>
  :root {
    --gold: #d3a42c;
    --gold-dark: #b98d1f;
    --teal: #17b1a6;
    --teal-dark: #0f9990;
    --ink: #2b2b2b;
    --body: #555;
    --muted: #6b6b6b;
    --blue: #2e8fc4;
    --footer: #3a3a3a;
    --top-bar: #444;
  }
  * { margin: 0; padding: 0; box-sizing: border-box; }
  html, body { width: 816px; height: 1200px; overflow: hidden; background: #fff; }
  body { position: relative; font-family: "Questrial", sans-serif; color: var(--body); }
  .abs { position: absolute; }

  .top-bar { left: 0; top: 0; width: 816px; height: 6px; background: var(--top-bar); }

  .brand { left: 66px; top: 58px; display: flex; align-items: center; gap: 8px; }
  .brand-mark { width: 12px; height: 12px; background: var(--gold); }
  .brand-name { font-size: 15px; color: var(--gold); letter-spacing: 0.4px; white-space: nowrap; }

  .contact { left: 630px; font-size: 12px; letter-spacing: 1.4px; color: var(--teal); display: flex; align-items: center; gap: 9px; }
  .contact svg { width: 14px; height: 14px; }

  .main-nav { left: 32px; top: 118px; width: 752px; height: 33px; background: linear-gradient(#dcb13e, #c99c25); }
  .main-nav a { position: absolute; top: 9px; font-size: 11px; letter-spacing: 0.8px; color: #fff; text-decoration: none; }

  .hero { left: 32px; top: 156px; width: 752px; height: 305px; background: linear-gradient(180deg, #3d86cf 0%, #8fbde4 40%, #efe6c8 55%, #d9cfae 72%, #4f8a2c 86%, #3c6d23 100%); }
  .hero-caption { left: 447px; top: 354px; width: 337px; height: 107px; background: rgba(40,40,40,0.78); color: #fff; padding: 14px 16px 0 16px; }
  .hero-caption h2 { font-weight: 400; font-size: 11px; letter-spacing: 0.6px; margin-bottom: 7px; }
  .hero-caption p { font-size: 8px; line-height: 13.6px; letter-spacing: 0.3px; text-align: justify; }

  .service { top: 494px; width: 180px; text-align: center; }
  .service-photo { display: block; width: 177px; height: 102px; border: 2px solid #fff; box-shadow: 1px 1px 3px rgba(0,0,0,0.25); }
  .service h3 { font-weight: 400; font-size: 12px; letter-spacing: 0.7px; color: var(--gold); margin-top: 11px; }
  .service p { font-size: 8px; line-height: 16px; letter-spacing: 0.4px; color: var(--muted); margin-top: 3px; }
  .btn { display: inline-block; background: var(--teal); color: #fff; font-size: 7.5px; letter-spacing: 0.6px; border-radius: 3px; padding: 6px 8px; border-bottom: 1px solid var(--teal-dark); }
  .service .btn { margin-top: 6px; }

  .divider { left: 76px; width: 648px; height: 1px; background: linear-gradient(90deg, rgba(211,164,44,0), var(--gold) 50%, rgba(211,164,44,0)); }

  .about { left: 100px; top: 748px; width: 616px; text-align: center; }
  .about h2 { font-weight: 400; font-size: 18px; letter-spacing: 1.2px; color: var(--ink); }
  .about p { font-family: "Arimo", sans-serif; font-size: 11px; line-height: 23px; color: var(--body); margin-top: 12px; }

  .feature-panel { left: 76px; top: 920px; width: 648px; height: 190px; background: linear-gradient(#ececec, #dcdcdc); border: 1px solid #d2d2d2; border-radius: 3px; box-shadow: 0 4px 6px -3px rgba(0,0,0,0.2); }
  .panel-title { font-size: 12px; letter-spacing: 0.8px; top: 947px; font-weight: 400; }
  .panel-rule { height: 3px; border-top: 1px solid #bbb; border-bottom: 1px solid #bbb; top: 967px; }
  .client-photo { left: 110px; top: 994px; width: 68px; height: 60px; background: linear-gradient(#f3f3f3, #c9b6a6); border: 3px solid #fff; box-shadow: 0 0 2px rgba(0,0,0,0.3); }
  .panel-text { font-family: "Arimo", sans-serif; font-size: 8.6px; line-height: 15.3px; color: var(--muted); text-align: justify; }
  .attribution { left: 188px; top: 1058px; width: 186px; text-align: right; font-family: "Arimo", sans-serif; font-style: italic; font-size: 8.6px; color: var(--blue); }
  .seal { left: 632px; top: 986px; width: 70px; height: 70px; border-radius: 50%; background: radial-gradient(circle at 40% 35%, #fbe27a, var(--gold) 70%, var(--gold-dark)); box-shadow: 1px 2px 3px rgba(0,0,0,0.25); }

  .site-footer { left: 0; top: 1157px; width: 816px; height: 43px; background: var(--footer); color: #ddd; font-size: 8px; letter-spacing: 1px; }
  .site-footer .links { position: absolute; left: 61px; top: 19px; }
  .site-footer .links span { margin: 0 9px; }
  .site-footer .copy { position: absolute; left: 326px; top: 18px; }
  .social { position: absolute; top: 9px; width: 19px; height: 19px; }
</style>
</head>
<body>
  <div class="abs top-bar"></div>

  <header class="abs brand">
    <span class="brand-mark"></span>
    <span class="brand-name">Kelbrook Painting</span>
  </header>

  <div class="abs contact" style="top:43px">
    <svg viewBox="0 0 16 16"><path d="M3 1l3 3-1.6 2a9 9 0 0 0 5.6 5.6L12 10l3 3-2 2C7 15 1 9 1 3z" fill="#17b1a6"/></svg>
    +123 456 7890
  </div>
  <div class="abs contact" style="top:67px">
    <svg viewBox="0 0 16 16"><rect x="1" y="3" width="14" height="10" fill="#17b1a6"/><path d="M1 3l7 6 7-6" fill="none" stroke="#fff" stroke-width="1.2"/></svg>
    your@email.com
  </div>

  <nav class="abs main-nav">
    <a style="left:35px">Home</a>
    <a style="left:126px">About us</a>
    <a style="left:233px">Services</a>
    <a style="left:337px">Testimonials</a>
    <a style="left:462px">Showcase</a>
    <a style="left:575px">Contact us</a>
  </nav>

  <div class="abs hero" role="img" aria-label="Photo of a cream two-storey house with tiled roof, arched windows and green lawn under a blue sky"></div>
  <div class="abs hero-caption">
    <h2>Welcome to Kelbrook Painting</h2>
    <p>Lorem ipsum dolor sit amet, consectetur adipiscing elit. Aenean accumsan sollicitudin mi at vehicula. Praesent nisl mi. Lorem ipsum dolor sit amet, consectetur adipiscing elit. Aenean accumsan sollicitudin mi at vehicula. Praesent nisl mi.</p>
  </div>

  <section class="abs service" style="left:68px">
    <span class="service-photo" role="img" aria-label="Photo of a yellow weatherboard house at dusk" style="background:linear-gradient(#7d8aa6,#c7a35a 55%,#d8c14e 70%,#4c5a2c)"></span>
    <h3>Residential Services</h3>
    <p>Lorem ipsum dolor sit amet, consectetur adipiscing elit. Aenean accumsan sollici-tudin mi at vehicula. Praesent nisl mi.</p>
    <span class="btn">Read more</span>
  </section>
  <section class="abs service" style="left:317px">
    <span class="service-photo" role="img" aria-label="Photo of a painter on scaffolding at a red shopfront mural" style="background:linear-gradient(90deg,#a8302e,#6b5d52 45%,#9b938a 70%,#b23a36)"></span>
    <h3>Commercial Services</h3>
    <p>Lorem ipsum dolor sit amet, consectetur adipiscing elit. Aenean accumsan sollici-tudin mi at vehicula. Praesent nisl mi.</p>
    <span class="btn">Read more</span>
  </section>
  <section class="abs service" style="left:570px">
    <span class="service-photo" role="img" aria-label="Photo of a construction crew in hard hats reviewing plans on site" style="background:linear-gradient(#b7c4d0,#8a7a66 55%,#c8c0a4)"></span>
    <h3>Strata Jobs</h3>
    <p>Lorem ipsum dolor sit amet, consectetur adipiscing elit. Aenean accumsan sollici-tudin mi at vehicula. Praesent nisl mi.</p>
    <span class="btn">Read more</span>
  </section>

  <div class="abs divider" style="top:733px"></div>
  <section class="abs about">
    <h2>About Us</h2>
    <p>Lorem ipsum dolor sit amet, consectetur adipiscing elit. Aenean accumsan sollicitudin mi at vehicula. Praesent nisl mi, molestie eget rutrum eget, sodales ac nisl. Vivamus neque felis, tempus et odio tempus, ultrices porta nibh. Nunc ultricies sapien bibendum, semper lectus id, convallis quam.</p>
  </section>
  <div class="abs divider" style="top:891px"></div>

  <div class="abs feature-panel"></div>
  <h3 class="abs panel-title" style="left:116px;color:var(--blue)">Client Testimonials</h3>
  <div class="abs panel-rule" style="left:114px;width:264px"></div>
  <div class="abs client-photo" role="img" aria-label="Portrait photo of a smiling client"></div>
  <p class="abs panel-text" style="left:188px;top:995px;width:190px">Lorem ipsum dolor sit amet, consectetur adipiscing elit. Aenean accumsan sollicitu-din mi at vehicula.Lorem ipsum dolor sit amet, consectetur adipiscing elit. Aenean</p>
  <div class="abs attribution">- Jane Doe,&nbsp; Restaurant Owner</div>
  <span class="abs btn" style="left:320px;top:1078px">Read more</span>

  <h3 class="abs panel-title" style="left:449px;color:var(--gold)">Satisfaction Guaranteed</h3>
  <div class="abs panel-rule" style="left:446px;width:264px"></div>
  <p class="abs panel-text" style="left:449px;top:991px;width:170px;text-align:left;line-height:16px">Lorem ipsum dolor sit amet, con-sectetur adipiscing elit. Aenean accumsan sollicitudin mi rutrum eget, sodales ac nisl.</p>
  <div class="abs seal"></div>

  <footer class="abs site-footer">
    <div class="links">Sitemap<span>|</span>Terms &amp; Conditions<span>|</span>FAQ</div>
    <div class="copy">Copyright @ 2013 Kelbrook Painting</div>
    <span class="social" style="left:645px;background:#3fb4e6"></span>
    <span class="social" style="left:669px;background:#3b5b9e"></span>
    <span class="social" style="left:694px;background:#f08a1c"></span>
  </footer>
</body>
</html>
```